Cutting edge/Modern brochure for #1 Indie real estate brokerage in the area.

Professional/Modern looking marketing brochures that we can leave behind after a listing or buyer presentation. We are the #1 local Indie Real Estate Company and a group of top producing agents broke away from the corporate real estate world. We just opened our second location which is 6,000 sq ft and a very modern design. Our website is www.pelvarhouses.com and our facebook page Tarnish Oak Real Estate Services has a sneak peak commercial of the new office to get inspiration. Attached is a file with verbiage and our logo with a black background and one with no background. We have cutting edge technology, offer 3D spherevue technology with virtual tours, radio show, etc...We want these pieces to be powerful to make the clients want to choose us!

Target Market(s)

We would like a brochure for buyers and one for sellers

Industry/Entity Type

Real Estate

Colors

Designer to choose colors to be used in the design.

Requirements
Must have
• Sleek, modern, professional look

```html
<!DOCTYPE html>
<html lang="en">
<head>
<meta charset="utf-8">
<title>Tarnish Oak Real Estate Services – Brochure Outside</title>
<link href="https://fonts.googleapis.com/css2?family=Montserrat:wght@300;400;500;600;800&display=swap" rel="stylesheet">
<style>
  :root {
    --gold: #b4923d;
    --gold-bright: #d8b83c;
    --gold-light: #ecd894;
    --gold-dark: #8a6b26;
    --ink: #111111;
    --black: #050505;
    --paper: #f7f7f6;
    --stage: #e4e4e4;
    --muted: #2b2b2b;
  }
  * { box-sizing: border-box; margin: 0; padding: 0; }
  html, body { width: 1200px; height: 828px; overflow: hidden; }
  body {
    background: var(--stage);
    font-family: "Montserrat", sans-serif;
    position: relative;
  }
  .brochure {
    position: absolute; left: 30px; top: 45px;
    width: 1140px; height: 738px;
    display: flex;
    background: var(--paper);
  }
  .panel { position: relative; width: 570px; height: 738px; overflow: hidden; }
  .gold-rule {
    position: absolute; left: 0; right: 0;
    background: linear-gradient(90deg, var(--gold-dark), var(--gold-light) 30%, var(--gold) 55%, var(--gold-light) 80%, var(--gold-dark));
  }

  /* Back panel */
  .back-photo {
    position: absolute; left: 0; top: 0; width: 570px; height: 280px;
    background: linear-gradient(180deg, #e9e9e9 0%, #d4d4d4 55%, #bdbdbd 100%);
  }
  .back-band { position: absolute; left: 0; top: 286px; width: 570px; height: 150px; background: var(--black); }
  .back-logo {
    position: absolute; left: 174px; top: 18px; width: 218px; height: 114px;
    background: #000;
    display: flex; flex-direction: column; align-items: center; justify-content: center;
    color: var(--gold-bright); font-weight: 600; text-align: center; line-height: 1.15;
  }
  .back-logo .name { font-size: 26px; letter-spacing: 1px; text-transform: uppercase; }
  .back-logo .sub { font-size: 10px; letter-spacing: 2px; text-transform: uppercase; margin-top: 6px; }

  .headline {
    position: absolute; left: 47px; top: 483px;
    font-size: 28px; font-weight: 300; letter-spacing: 0.5px; color: var(--ink);
  }
  .headline .accent { color: var(--gold); }

  .contact { position: absolute; left: 40px; top: 562px; color: var(--ink); }
  .contact .touch { font-size: 14px; font-weight: 400; }
  .contact .touch .accent { color: var(--gold); font-weight: 500; }
  .contact .touch::after {
    content: ""; display: block; width: 34px; height: 1px; background: var(--gold); margin-top: 2px;
  }
  .contact .company { margin-top: 12px; font-size: 15px; line-height: 1.15; }
  .contact .company .firm { color: var(--gold); font-weight: 600; text-transform: uppercase; }
  .contact .company .line { font-weight: 400; }
  .contact ul { list-style: none; margin-top: 10px; }
  .contact li {
    display: flex; align-items: center; gap: 10px;
    font-size: 11.5px; color: var(--muted); height: 19.6px;
  }
  .contact li svg { width: 11px; height: 11px; flex: none; }

  .badges {
    position: absolute; left: 322px; top: 688px;
    display: flex; align-items: center; gap: 7px;
  }
  .badge { height: 22px; border-radius: 3px; }
  .badge.wide { width: 62px; background: #1f5a8c; }
  .badge.tile { width: 22px; }
  .badge.blue { background: #3b5a9a; }
  .badge.violet { background: #c1306a; }
  .badge.red { background: #dd4b39; }
  .badge.green { width: 22px; background: #3a8f6a; border-radius: 50%; }
  .badge.pale { width: 42px; background: #d9d9d9; }

  /* Front panel */
  .front-top { position: absolute; left: 0; top: 0; width: 570px; height: 437px; background: var(--paper); }
  .front-base { position: absolute; left: 0; top: 437px; width: 570px; height: 290px; background: var(--black); }
  .front-photo {
    position: absolute; left: 51px; top: 44px; width: 472px; height: 483px;
    background: linear-gradient(135deg, #c9a46a 0%, #9b7a4c 35%, #5a5348 65%, #8c8173 100%);
  }
  .photo-frame {
    position: absolute; left: 18px; top: 18px; right: 18px; bottom: 18px;
    border: 1px solid rgba(255,255,255,0.55);
  }
  .claim {
    position: absolute; left: 127px; top: 133px; width: 218px; height: 218px;
    background: rgba(20,20,20,0.78);
    display: flex; flex-direction: column; align-items: center; justify-content: center;
    color: #fff; text-align: center; padding-bottom: 30px;
  }
  .claim .lead { font-size: 18px; font-weight: 400; line-height: 1.1; text-transform: uppercase; }
  .claim .rank { font-size: 33px; font-weight: 800; color: var(--gold-bright); margin-top: 4px; line-height: 1.1; }
  .claim .kind { font-size: 18px; font-weight: 400; letter-spacing: 5px; margin-top: 4px; text-transform: uppercase; }

  .front-logo {
    position: absolute; left: 0; width: 570px; top: 563px;
    text-align: center; color: var(--gold-bright); font-weight: 600; line-height: 1.15;
  }
  .front-logo .name { font-size: 38px; letter-spacing: 1.5px; text-transform: uppercase; }
  .front-logo .sub { font-size: 13px; letter-spacing: 3px; text-transform: uppercase; margin-top: 10px; }
  .front-url {
    position: absolute; left: 0; width: 570px; top: 703px;
    text-align: center; color: #e9e9e9; font-size: 10px; letter-spacing: 4px; text-transform: uppercase;
  }
</style>
</head>
<body>
  <main class="brochure">
    <section class="panel back">
      <div class="back-photo" role="img" aria-label="Black and white photo of a bright dining nook with a wooden table, chairs, chandelier and tall windows overlooking hills"></div>
      <div class="gold-rule" style="top:280px;height:6px"></div>
      <div class="back-band">
        <div class="back-logo">
          <span class="name">Tarnish Oak</span>
          <span class="sub">Real Estate Services</span>
        </div>
      </div>
      <div class="gold-rule" style="top:436px;height:5px"></div>

      <h2 class="headline"><span class="accent">DON’T TAKE</span> OUR WORD FOR IT!</h2>

      <div class="contact">
        <p class="touch"><span class="accent">Get In</span> Touch</p>
        <p class="company"><span class="firm">Tarnish Oak</span><br><span class="line">Real Estate Services</span></p>
        <ul>
          <li><svg viewBox="0 0 12 12"><circle cx="6" cy="6" r="6" fill="#b4923d"/><path d="M6 2.6a2.2 2.2 0 0 0-2.2 2.2C3.8 6.6 6 9.4 6 9.4s2.2-2.8 2.2-4.6A2.2 2.2 0 0 0 6 2.6z" fill="#fff"/></svg>Address Goes Here</li>
          <li><svg viewBox="0 0 12 12"><circle cx="6" cy="6" r="6" fill="#b4923d"/><path d="M4 3l1.2 1.4-.6.8c.4.9 1.1 1.6 2 2l.8-.6L9 7.8 8.2 9C6 8.8 3.2 6 3 3.8z" fill="#fff"/></svg>+0123 456 789</li>
          <li><svg viewBox="0 0 12 12"><circle cx="6" cy="6" r="6" fill="#b4923d"/><rect x="3" y="4" width="6" height="4" fill="#fff"/><path d="M3 4l3 2.2L9 4" stroke="#b4923d" stroke-width=".7" fill="none"/></svg>Info@yourmailid.com</li>
          <li><svg viewBox="0 0 12 12"><circle cx="6" cy="6" r="6" fill="#b4923d"/><circle cx="6" cy="6" r="2.8" fill="none" stroke="#fff" stroke-width=".8"/></svg>www.pelvarhouses.com</li>
        </ul>
      </div>

      <div class="badges" aria-label="Partner and social profiles">
        <span class="badge wide"></span>
        <span class="badge green"></span>
        <span class="badge tile blue"></span>
        <span class="badge tile violet"></span>
        <span class="badge tile red"></span>
        <span class="badge pale"></span>
      </div>
    </section>

    <section class="panel front">
      <div class="front-top"></div>
      <div class="front-base"></div>
      <div class="front-photo" role="img" aria-label="Warm-toned photo of a vaulted living room with a grey sectional, tufted ottoman, ceiling fan, mountain-view windows and an open wood kitchen">
        <div class="photo-frame"></div>
        <div class="claim">
          <span class="lead">We are the<br>area’s</span>
          <span class="rank">#1 INDIE</span>
          <span class="kind">Brokerage</span>
        </div>
      </div>
      <div class="front-logo">
        <div class="name">Tarnish Oak</div>
        <div class="sub">Real Estate Services</div>
      </div>
      <div class="front-url">www.pelvarhouses.com</div>
    </section>

    <div class="gold-rule" style="top:727px;height:11px"></div>
  </main>
</body>
</html>
```